Business Cards/Stationary for Statistical Consulting Firm
Cobalt Heron Analytics Group, LLC
Business Cards/Stationary for Statistical Consulting Firm - Consulting
Creative Brief
Use same font as used in my logo
Feel free to try new fonts.
Professional
Trevor Dunne-Morcott
Statistical Analyst
517 Upper Kestling Rd Alderbrook, VT 05491
1-855-7GET-DATA
trevor@cobaltheronanalytics.example
www.cobaltheronanalytics.example
Single and Double Sided designs are both okay. Feel free to try different variations of the logo. Look at the website (www.cobaltheronanalytics.example) for ideas.

```html
<!DOCTYPE html>
<html lang="en">
<head>
<meta charset="utf-8">
<title>Cobalt Heron Analytics Group – Business Card</title>
<link rel="stylesheet" href="https://fonts.googleapis.com/css2?family=Cinzel:wght@400&family=Lato:wght@300;400&display=swap">
<style>
  :root {
    --page: #e9e6e1;
    --ink: #111111;
    --card-white: #fafafa;
    --card-black: #141414;
    --grey: #8c8c8c;
    --light: #eeeeee;
    --muted: #555555;
  }
  * { box-sizing: border-box; margin: 0; padding: 0; }
  html, body { width: 1200px; height: 1023px; overflow: hidden; }
  body {
    background: var(--page);
    font-family: "Lato", Arial, sans-serif;
    position: relative;
  }
  .card {
    position: absolute;
    left: 220px;
    width: 760px;
    height: 434px;
    border-radius: 6px;
    overflow: hidden;
    box-shadow: 0 10px 28px rgba(0,0,0,0.25);
  }
  .card-front { top: 48px; background: var(--card-white); }
  .card-back { top: 542px; background: var(--card-black); }
  .front-shape { position: absolute; inset: 0; }

  .holder {
    position: absolute; left: 48px; top: 46px;
    color: var(--ink);
  }
  .holder-name { font-size: 28px; font-weight: 400; letter-spacing: 0.3px; }
  .holder-title { font-size: 15px; font-weight: 300; color: var(--muted); margin-top: 4px; letter-spacing: 1px; }

  .brand {
    position: absolute; left: 48px; bottom: 60px;
    display: flex; align-items: center; gap: 16px;
  }
  .brand-dot { width: 44px; height: 44px; border-radius: 50%; background: var(--ink); flex: none; }
  .brand-text { display: flex; flex-direction: column; }
  .brand-name {
    font-family: "Cinzel", Georgia, serif; font-size: 30px;
    color: var(--ink); letter-spacing: 2px; line-height: 1;
  }
  .brand-sub {
    font-family: "Cinzel", Georgia, serif; font-size: 12px;
    color: var(--ink); letter-spacing: 4px; margin-top: 6px;
  }

  .contact {
    position: absolute; right: 44px; top: 150px;
    color: var(--light); font-size: 15px; font-weight: 300;
    line-height: 1.7; text-align: right;
  }
  .contact-group + .contact-group { margin-top: 12px; }

  .back-brand {
    position: absolute; inset: 0;
    display: flex; flex-direction: column; align-items: center; justify-content: center;
  }
  .back-brand .brand-row { display: flex; align-items: center; gap: 18px; }
  .back-brand .brand-dot { background: var(--light); width: 40px; height: 40px; }
  .back-brand .brand-name { color: var(--light); font-size: 44px; letter-spacing: 4px; }
  .back-brand .brand-sub { color: var(--light); font-size: 15px; letter-spacing: 5px; margin-top: 12px; }
</style>
</head>
<body>
  <section class="card card-front">
    <svg class="front-shape" width="760" height="434" viewBox="0 0 760 434" aria-hidden="true">
      <path d="M440 0 C 330 110, 560 300, 400 434 L 760 434 L 760 0 Z" fill="var(--card-black)"/>
      <path d="M418 0 C 305 110, 535 300, 376 434" fill="none" stroke="var(--grey)" stroke-width="4"/>
      <path d="M400 0 C 285 110, 515 300, 356 434" fill="none" stroke="#cfcfcf" stroke-width="1.5"/>
    </svg>
    <div class="holder">
      <p class="holder-name">Trevor Dunne-Morcott</p>
      <p class="holder-title">Statistical Analyst</p>
    </div>
    <div class="brand">
      <span class="brand-dot"></span>
      <div class="brand-text">
        <span class="brand-name">Cobalt Heron</span>
        <span class="brand-sub">Analytics Group</span>
      </div>
    </div>
    <div class="contact">
      <div class="contact-group">
        <p>517 Upper Kestling Rd</p>
        <p>Alderbrook, VT 05491</p>
      </div>
      <div class="contact-group">
        <p>1-855-7GET-DATA</p>
      </div>
      <div class="contact-group">
        <p>trevor@cobaltheronanalytics.example</p>
        <p>www.cobaltheronanalytics.example</p>
      </div>
    </div>
  </section>

  <section class="card card-back">
    <div class="back-brand">
      <div class="brand-row">
        <span class="brand-dot"></span>
        <span class="brand-name">Cobalt Heron</span>
      </div>
      <span class="brand-sub">Analytics Group</span>
    </div>
  </section>
</body>
</html>
```